Mirabo & Orvan Automotive Repair Shop. Need a new website design.

We specialize in Mirabo & Orvan auto repair, but also work on other Asian import vehicles. We have been in business for 7 years and pride ourselves on high quality auto repair that is fixed right the first time. Would like the automotive repair website to incorporate the colors black, red and white if possible and have our logo and some Mirabo and Orvan vehicles included in the website.

Target Market(s)

Mirabo & Orvan vehicle owners

Industry/Entity Type

Automotive Repair

Coding

Coded - Design and coding required

Number of Pages Required

5+ page

Colors
EB3D1F
EC4F4E
F09395
F8D3D4
FCEDEE

Requirements
Must have
• Home, Services, Contact Us, Schedule appointment, and a gallery tab that I can add shop pictures to when completed.
Nice to have
• Would like to see example pictures of job next to each service listed.
Should not have
• Service not related to auto repair. Ex. auto detailing, towing, car wash

```html
<!DOCTYPE html>
<html lang="en">
<head>
<meta charset="utf-8">
<title>Halden Automotive</title>
<link rel="stylesheet" href="https://fonts.googleapis.com/css2?family=Krona+One&family=Roboto:wght@400;500;700;900&display=swap">
<style>
:root{
  --red:#e3000f;
  --black:#000;
  --panel:#161616;
  --card:#1b1b1b;
  --field:#161616;
  --field-line:#2e2e2e;
  --white:#fff;
  --text:#d6d6d6;
  --gold:#f7b21b;
  --footer:#0f0f0f;
}
*{box-sizing:border-box;margin:0;padding:0}
html,body{width:1200px;height:5293px;overflow:hidden;background:var(--black)}
body{font-family:"Roboto",Arial,sans-serif;color:var(--white);position:relative}
.page{position:relative;width:1200px;height:5293px;overflow:hidden}
.abs{position:absolute}
.heading{font-family:"Krona One",sans-serif;font-size:30px;letter-spacing:2px;text-transform:uppercase;line-height:40px;
  background:linear-gradient(180deg,#f0f0f0,#8d8d8d);-webkit-background-clip:text;background-clip:text;color:transparent;white-space:nowrap}
.heading.center{left:0;width:1200px;text-align:center}
.heading.light{background:none;color:var(--white)}
.underline{position:absolute;height:5px;width:76px;left:562px;background:var(--red);border-radius:2px}
.btn{position:absolute;display:flex;align-items:center;justify-content:center;gap:7px;background:var(--red);color:var(--white);
  font-weight:700;font-size:14px;text-transform:uppercase;border-radius:5px;box-shadow:0 0 0 2px #fff inset, 0 0 0 4px var(--red) inset}
.btn svg{width:14px;height:14px}

.topbar{top:0;left:0;width:1200px;height:37px;background:var(--red);font-size:13px;font-weight:500}
.topbar span{position:absolute;top:10px;display:flex;gap:6px;align-items:center}
.nav{top:37px;left:0;width:1200px;height:83px;background:rgba(0,0,0,.88);z-index:3}
.nav a{position:absolute;top:32px;color:var(--white);font-size:14px;font-weight:500;text-decoration:none}
.nav .cta{top:20px;left:921px;width:137px;height:38px;font-size:14px;text-transform:none}
.brandmark{top:0;left:514px;width:172px;height:184px;z-index:4}
.brandmark .name{position:absolute;top:74px;left:0;width:172px;text-align:center;font-family:"Krona One",sans-serif;font-size:19px;color:var(--white)}

.hero-photo{top:37px;left:0;width:1200px;height:826px;background:radial-gradient(ellipse at 45% 40%,#6c5a25 0%,#2b2f35 35%,#111418 70%,#07080a 100%)}
.hero-title{top:330px;left:0;width:1200px;text-align:center;font-family:"Krona One",sans-serif;font-size:40px;letter-spacing:2px;color:var(--white)}
.hero-text{top:400px;left:250px;width:700px;text-align:center;font-size:13.5px;line-height:25px;font-weight:500}
.dots{top:767px;left:556px;display:flex;gap:6px}
.dots i{width:12px;height:12px;border-radius:50%;border:1.5px solid #ddd;display:block}
.dots i.on{background:var(--red);border-color:var(--red)}

.about-text{left:649px;width:407px;font-size:12.5px;line-height:21.5px;color:var(--text);text-align:justify}

.services{top:1459px;left:0;width:1200px;height:569px;background:var(--panel)}
.svc{position:absolute;width:220px}
.svc .img{width:220px}
.svc p{text-align:center;font-size:15px;font-weight:700;margin-top:14px}
.arrow{position:absolute;width:26px;height:30px}

.brand-row{position:absolute;display:flex;align-items:center;gap:14px;font-size:15px}
.brand-row i{display:block;width:52px;height:52px;border-radius:50%;background:#1f1f1f;border:1px solid #333}

.tcard{position:absolute;top:2669px;width:378px;height:214px;background:var(--card);border-radius:26px}
.avatar{position:absolute;top:2700px;width:108px;height:108px;border-radius:50%;border:4px solid #222;background:radial-gradient(circle at 50% 40%,#b89a86,#5d5a58 70%)}
.quote{position:absolute;font-family:Georgia,serif;font-size:56px;line-height:1;color:var(--red);font-weight:700}
.ttext{position:absolute;width:260px;font-size:13px;line-height:22px;color:var(--text)}
.tname{position:absolute;font-size:15px;font-weight:700}
.stars{position:absolute;color:var(--gold);font-size:15px;letter-spacing:2px}

.certs{top:2990px;left:0;width:1200px;height:298px;background:linear-gradient(90deg,#ec0a0a 0%,#c10808 45%,#5e0a0a 100%)}
.badge{position:absolute;top:3140px;width:96px;height:96px;border-radius:50%;background:rgba(255,255,255,.92)}

.gallery{top:3288px;left:0;width:1200px;height:668px;background:var(--panel)}
.gimg{position:absolute}

.field{position:absolute;height:44px;background:var(--field);border:1px solid var(--field-line);border-radius:3px;font-size:12px;color:#9a9a9a;padding:13px 16px}

.schedule{top:4578px;left:0;width:1200px;height:412px;background:linear-gradient(90deg,#ef0a0a 0%,#bd0909 50%,#5c0a0a 100%)}

.footer{top:4990px;left:0;width:1200px;height:303px;background:var(--footer)}
.fcol h4{font-size:15px;font-weight:700;margin-bottom:14px}
.fcol a{display:block;color:var(--text);text-decoration:none;font-size:12px;line-height:24px}
.fcol{position:absolute;top:5000px}
.finfo{display:flex;gap:10px;margin-bottom:10px;font-size:12px;line-height:18px;color:var(--text)}
.finfo b{display:block;color:var(--white);font-size:11px}
.finfo svg{flex:none;width:14px;height:14px;margin-top:2px}
.social{position:absolute;top:5148px;width:27px;height:27px;background:#fff;border-radius:3px}
</style>
</head>
<body>
<div class="page">

  <div class="abs hero-photo" role="img" aria-label="Close-up of engine pistons splashed with golden motor oil"></div>

  <div class="abs topbar">
    <span style="left:144px">
      <svg width="12" height="12" viewBox="0 0 24 24" fill="#fff"><path d="M6.6 10.8a15 15 0 0 0 6.6 6.6l2.2-2.2a1 1 0 0 1 1-.25 11.4 11.4 0 0 0 3.6.57 1 1 0 0 1 1 1V20a1 1 0 0 1-1 1A17 17 0 0 1 3 4a1 1 0 0 1 1-1h3.5a1 1 0 0 1 1 1c0 1.25.2 2.45.57 3.57a1 1 0 0 1-.25 1z"/></svg>
      555.010.7493</span>
    <span style="left:281px">
      <svg width="13" height="12" viewBox="0 0 24 20" fill="#fff"><path d="M2 2h20v16H2z M2 2l10 8 10-8" stroke="#e3000f" stroke-width="1.6"/></svg>
      hello@haldenauto.example</span>
    <span style="right:146px">
      <svg width="12" height="12" viewBox="0 0 24 24"><circle cx="12" cy="12" r="10" fill="none" stroke="#fff" stroke-width="2.4"/><path d="M12 6v6l4 3" stroke="#fff" stroke-width="2.4" fill="none"/></svg>
      Hours of Operation: M-F 8:30-6pm</span>
  </div>

  <nav class="abs nav">
    <a style="left:144px">Home</a>
    <a style="left:201px">About Us</a>
    <a style="left:279px">Vehicles</a>
    <a style="left:353px">Services</a>
    <a style="left:427px">Locations</a>
    <a style="left:705px">Shop Tours</a>
    <a style="left:796px">Blog</a>
    <a style="left:843px">Careers</a>
    <span class="btn cta">Schedule Service</span>
  </nav>

  <div class="abs brandmark">
    <svg width="172" height="184" viewBox="0 0 172 184"><polygon points="86,2 168,46 168,138 86,182 4,138 4,46" fill="#0b0b0b" stroke="#1e1e1e" stroke-width="3"/></svg>
    <div class="name">HALDEN</div>
  </div>

  <h1 class="abs hero-title">HALDEN AUTOMOTIVE</h1>
  <p class="abs hero-text">Halden Automotive is a locally owned and operated auto repair shop in Brookvale that offers comprehensive car care and services for Mirabo &amp; Orvan and all other Asian imports vehicles.</p>
  <span class="btn" style="top:479px;left:490px;width:222px;height:51px">Schedule Service
    <svg viewBox="0 0 16 16"><circle cx="8" cy="8" r="7" fill="#fff"/><path d="M7 5l3 3-3 3" stroke="#e3000f" stroke-width="2" fill="none"/></svg></span>

  <div class="abs dots"><i></i><i></i><i class="on"></i><i></i><i></i></div>

  <svg class="abs" style="top:690px;left:0" width="1200" height="175" viewBox="0 0 1200 175">
    <defs><linearGradient id="silverA" x1="0" x2="1"><stop offset="0" stop-color="#555"/><stop offset=".5" stop-color="#e6e6e6"/><stop offset="1" stop-color="#8a8a8a"/></linearGradient></defs>
    <polygon points="600,150 1200,8 1200,30 600,174" fill="url(#silverA)"/>
    <polygon points="0,22 600,174 1200,30 1200,175 0,175" fill="#000"/>
  </svg>

  <!-- About -->
  <svg class="abs" style="top:908px;left:144px" width="432" height="482" viewBox="0 0 432 482" role="img" aria-label="Two technicians repairing a car engine in the shop, framed by a red shield">
    <defs><linearGradient id="shop" x1="0" y1="0" x2="1" y2="1"><stop offset="0" stop-color="#5a5f66"/><stop offset=".5" stop-color="#2d3036"/><stop offset="1" stop-color="#18191c"/></linearGradient></defs>
    <path d="M216 4 L428 50 Q430 330 216 478 Q2 330 4 50 Z" fill="#c4000d"/>
    <path d="M216 20 L412 62 Q412 320 216 460 Q20 320 20 62 Z" fill="#111"/>
    <path d="M216 34 L398 74 Q396 310 216 444 Q36 310 34 74 Z" fill="url(#shop)"/>
  </svg>
  <h2 class="abs heading" style="top:993px;left:649px">About Us</h2>
  <span class="abs" style="top:1012px;left:910px;width:76px;height:4px;background:var(--red)"></span>
  <p class="abs about-text" style="top:1058px">Led by an NAT master certified technician with 20 years experience working for Mirabo &amp; Orvan dealerships, our auto shop is your go to facility for everything from factory auto maintenance, including oil changes, fluid services and tune ups, to complex engine repairs, hybrid diagnostic &amp; repair, brake jobs, etc.</p>
  <p class="abs about-text" style="top:1180px">We have state of the art equipment and tools to ensure that we can properly diagnose and repair your vehicle to get you back on the road quickly. All of our work comes with a warranty for your peace of mind. We also offer discounts for RideNow &amp; Lumo rides.</p>
  <span class="btn" style="top:1303px;left:647px;width:144px;height:43px">Read More
    <svg viewBox="0 0 16 16"><circle cx="8" cy="8" r="7" fill="#fff"/><path d="M7 5l3 3-3 3" stroke="#e3000f" stroke-width="2" fill="none"/></svg></span>

  <!-- Services -->
  <section class="abs services" role="img" aria-label="Dark honeycomb texture background"></section>
  <h2 class="abs heading center" style="top:1514px">Our Services</h2>
  <span class="underline" style="top:1566px"></span>

  <svg class="arrow" style="top:1769px;left:78px" viewBox="0 0 26 30"><path d="M18 4L7 15l11 11" stroke="#ccc" stroke-width="4" fill="none"/></svg>
  <svg class="arrow" style="top:1769px;left:1097px" viewBox="0 0 26 30"><path d="M8 4l11 11L8 26" stroke="#ccc" stroke-width="4" fill="none"/></svg>

  <div class="svc" style="top:1619px;left:144px">
    <div class="img" style="height:282px;background:linear-gradient(160deg,#3a3f46,#15171a 60%,#6a4a10)" role="img" aria-label="Fresh oil being poured into an engine"></div>
    <p>Oil Changes</p>
  </div>
  <div class="svc" style="top:1644px;left:374px">
    <div class="img" style="height:277px;background:linear-gradient(160deg,#4a4f57,#22252a 60%,#5a4030)" role="img" aria-label="Mechanic running computer diagnostics on a laptop under the hood"></div>
    <p>Computer Diagnostics</p>
  </div>
  <div class="svc" style="top:1619px;left:605px">
    <div class="img" style="height:282px;background:linear-gradient(160deg,#7a4a22,#2c2a2a 55%,#1d2430)" role="img" aria-label="Technician testing electrical wiring in an engine bay"></div>
    <p>Electrical Specialists</p>
  </div>
  <div class="svc" style="top:1644px;left:836px">
    <div class="img" style="height:277px;background:linear-gradient(160deg,#5c5e62,#2a2c30 55%,#6a3a1a)" role="img" aria-label="Two mechanics changing a tire on a lifted vehicle"></div>
    <p>Tires</p>
  </div>

  <!-- Brands -->
  <svg class="abs" style="top:2028px;left:0" width="590" height="454" viewBox="0 0 590 454" role="img" aria-label="Dark blue Mirabo SUV parked in the service bay">
    <defs>
      <linearGradient id="suv" x1="0" y1="0" x2="1" y2="1"><stop offset="0" stop-color="#b9bec4"/><stop offset=".45" stop-color="#3f4652"/><stop offset="1" stop-color="#15181e"/></linearGradient>
      <linearGradient id="silverB" x1="0" y1="0" x2="0" y2="1"><stop offset="0" stop-color="#eee"/><stop offset=".5" stop-color="#888"/><stop offset="1" stop-color="#ddd"/></linearGradient>
    </defs>
    <polygon points="0,0 545,0 575,227 535,454 0,454" fill="url(#suv)"/>
    <polyline points="545,0 585,227 545,454" fill="none" stroke="url(#silverB)" stroke-width="8"/>
  </svg>
  <h2 class="abs heading" style="top:2104px;left:617px">Our Brands</h2>
  <span class="abs" style="top:2122px;left:959px;width:74px;height:4px;background:var(--red)"></span>
  <p class="abs" style="top:2158px;left:617px;width:400px;font-size:12.5px;line-height:24px;color:var(--text)">Halden Automotive specializes in Mirabo &amp; Orvan auto repair but also service and repair the following makes</p>

  <div class="brand-row" style="top:2247px;left:617px"><i></i>Sorano</div>
  <div class="brand-row" style="top:2247px;left:775px"><i></i>Kaveri</div>
  <div class="brand-row" style="top:2247px;left:944px"><i></i>Altura</div>
  <div class="brand-row" style="top:2327px;left:617px"><i></i>Velo</div>
  <div class="brand-row" style="top:2327px;left:775px"><i></i>Norikan</div>
  <div class="brand-row" style="top:2327px;left:944px"><i></i>Tsurumi</div>
  <div class="brand-row" style="top:2407px;left:617px"><i></i>Ambrose</div>
  <div class="brand-row" style="top:2407px;left:775px"><i></i>Kazuma</div>

  <!-- Testimonials -->
  <h2 class="abs heading center" style="top:2563px">What Our Clients Say</h2>
  <span class="underline" style="top:2615px"></span>

  <svg class="arrow" style="top:2760px;left:78px" viewBox="0 0 26 30"><path d="M18 4L7 15l11 11" stroke="#ccc" stroke-width="4" fill="none"/></svg>
  <svg class="arrow" style="top:2760px;left:1097px" viewBox="0 0 26 30"><path d="M8 4l11 11L8 26" stroke="#ccc" stroke-width="4" fill="none"/></svg>

  <div class="tcard" style="left:208px"></div>
  <div class="avatar" style="left:158px" role="img" aria-label="Client portrait"></div>
  <div class="quote" style="top:2688px;left:298px">&ldquo;</div>
  <p class="ttext" style="top:2733px;left:300px">Sed ut perspiciatis unde omnis iste natus sit voluptatem accusantium doloremque laudantium, totam rem aperiam,</p>
  <div class="tname" style="top:2814px;left:300px">John Doe</div>
  <div class="stars" style="top:2836px;left:300px">★★★★★</div>

  <div class="tcard" style="left:664px"></div>
  <div class="avatar" style="left:614px" role="img" aria-label="Client portrait"></div>
  <div class="quote" style="top:2688px;left:754px">&ldquo;</div>
  <p class="ttext" style="top:2733px;left:756px">Sed ut perspiciatis unde omnis iste natus sit voluptatem accusantium doloremque laudantium, totam rem aperiam,</p>
  <div class="tname" style="top:2814px;left:756px">John Doe</div>
  <div class="stars" style="top:2836px;left:756px">★★★★★</div>

  <!-- Certificates -->
  <section class="abs certs"></section>
  <h2 class="abs heading center light" style="top:3040px">Certificate &amp; Installer</h2>
  <span class="abs" style="top:3092px;left:574px;width:52px;height:4px;background:#fff"></span>
  <span class="badge" style="left:250px" role="img" aria-label="Partner badge"></span>
  <span class="badge" style="left:450px" role="img" aria-label="Partner badge"></span>
  <span class="badge" style="left:650px" role="img" aria-label="Award badge"></span>
  <span class="badge" style="left:850px" role="img" aria-label="Certification badge"></span>

  <!-- Gallery -->
  <section class="abs gallery" role="img" aria-label="Dark honeycomb texture background"></section>
  <h2 class="abs heading center" style="top:3353px">Our Gallery</h2>
  <span class="underline" style="top:3405px"></span>
  <div class="gimg" style="top:3450px;left:144px;width:222px;height:434px;background:linear-gradient(180deg,#4c5560,#262a30 50%,#5a1414)" role="img" aria-label="Mechanic draining oil under a lifted car"></div>
  <div class="gimg" style="top:3450px;left:374px;width:222px;height:213px;background:linear-gradient(160deg,#8b9098,#3d434c)" role="img" aria-label="Sedan with hood open on a lift"></div>
  <div class="gimg" style="top:3450px;left:604px;width:222px;height:213px;background:linear-gradient(160deg,#a6aab0,#30363f 70%,#2b4c8c)" role="img" aria-label="Service bay with a pickup truck on a blue lift"></div>
  <div class="gimg" style="top:3671px;left:374px;width:222px;height:213px;background:linear-gradient(180deg,#7aa6d8,#c9c4b8 55%,#6a6660)" role="img" aria-label="Shop exterior with a silver minivan parked"></div>
  <div class="gimg" style="top:3671px;left:604px;width:222px;height:213px;background:linear-gradient(160deg,#8a8f96,#2f5fa8 60%,#1d2230)" role="img" aria-label="Blue car raised on a lift in the service bay"></div>
  <div class="gimg" style="top:3450px;left:834px;width:222px;height:434px;background:linear-gradient(180deg,#b5b8bc,#555a62 45%,#2a2c30)" role="img" aria-label="Technician working under a car raised on a lift"></div>

  <!-- Contact -->
  <h2 class="abs heading center" style="top:4021px">Contact Us</h2>
  <span class="underline" style="top:4073px"></span>
  <div class="field" style="top:4128px;left:144px;width:292px">Name</div>
  <div class="field" style="top:4128px;left:452px;width:294px">Phone</div>
  <div class="field" style="top:4128px;left:762px;width:294px">Email Address</div>
  <div class="field" style="top:4194px;left:144px;width:448px">Year</div>
  <div class="field" style="top:4194px;left:608px;width:448px">Make</div>
  <div class="field" style="top:4260px;left:144px;width:448px">Model</div>
  <div class="field" style="top:4260px;left:608px;width:448px">Services
    <svg style="position:absolute;right:18px;top:19px" width="10" height="6" viewBox="0 0 10 6"><path d="M0 0h10L5 6z" fill="#aaa"/></svg></div>
  <div class="field" style="top:4326px;left:144px;width:912px;height:84px">Message</div>
  <span class="btn" style="top:4455px;left:530px;width:140px;height:44px">Submit
    <svg viewBox="0 0 16 16"><circle cx="8" cy="8" r="7" fill="#fff"/><path d="M7 5l3 3-3 3" stroke="#e3000f" stroke-width="2" fill="none"/></svg></span>

  <!-- Schedule -->
  <section class="abs schedule"></section>
  <h2 class="abs heading center light" style="top:4633px">Schedule An Appointment</h2>
  <svg class="abs" style="top:4716px;left:290px" width="40" height="40" viewBox="0 0 40 40"><circle cx="20" cy="20" r="19" fill="#fff"/><circle cx="20" cy="20" r="14" fill="none" stroke="#e3000f" stroke-width="2"/><path d="M15 13l3 3-2 2a11 11 0 0 0 6 6l2-2 3 3-2 2c-6 0-13-7-13-13z" fill="#e3000f"/></svg>
  <div class="abs" style="top:4712px;left:344px;font-size:14px;font-weight:700">Contact us for a free estimate!</div>
  <div class="abs" style="top:4733px;left:344px;font-size:26px;font-weight:500">Call: <b>555.010.9110</b></div>
  <svg class="abs" style="top:4698px;left:620px" width="110" height="30" viewBox="0 0 110 30"><path d="M4 22 Q50 -4 100 14" stroke="#fff" stroke-width="2" fill="none"/><path d="M92 8l9 6-10 3" stroke="#fff" stroke-width="2" fill="none"/></svg>
  <div class="abs" style="top:4720px;left:662px;font-family:Georgia,serif;font-style:italic;font-size:28px;font-weight:700">or</div>
  <span class="btn" style="top:4722px;left:762px;width:178px;height:46px">Free Estimate
    <svg viewBox="0 0 16 16"><circle cx="8" cy="8" r="7" fill="#fff"/><path d="M7 5l3 3-3 3" stroke="#e3000f" stroke-width="2" fill="none"/></svg></span>

  <!-- Footer -->
  <svg class="abs" style="top:4840px;left:0" width="1200" height="152" viewBox="0 0 1200 152">
    <defs><linearGradient id="silverC" x1="0" x2="1"><stop offset="0" stop-color="#444"/><stop offset=".5" stop-color="#f0f0f0"/><stop offset="1" stop-color="#444"/></linearGradient></defs>
    <polygon points="0,126 600,0 1200,126 1200,144 600,22 0,144" fill="url(#silverC)"/>
    <polygon points="0,144 600,22 1200,144 1200,152 0,152" fill="#0f0f0f"/>
  </svg>
  <section class="abs footer"></section>

  <div class="abs" style="top:4983px;left:154px;width:154px;height:150px">
    <svg width="154" height="150" viewBox="0 0 154 150"><polygon points="77,2 150,38 150,112 77,148 4,112 4,38" fill="#0b0b0b" stroke="#c4000d" stroke-width="3"/></svg>
    <div style="position:absolute;top:64px;left:0;width:154px;text-align:center;font-family:'Krona One',sans-serif;font-size:17px;color:#fff">HALDEN</div>
  </div>
  <span class="social" style="left:163px" aria-label="Social profile"></span>
  <span class="social" style="left:200px" aria-label="Social profile"></span>
  <span class="social" style="left:237px" aria-label="Social profile"></span>
  <span class="social" style="left:274px" aria-label="Social profile"></span>

  <div class="fcol" style="left:446px">
    <h4>Quick Links</h4>
    <a>Home</a><a>About Us</a><a>Services</a><a>Our Projects</a><a>Contact Us</a>
  </div>
  <div class="fcol" style="left:625px">
    <h4>About Company</h4>
    <a>Terms of Use</a><a>Terms &amp; Condition</a><a>Areas We Serve</a><a>Careers</a><a>Sitemap</a>
  </div>
  <div class="fcol" style="left:832px;width:240px">
    <h4>Contact Us</h4>
    <div class="finfo"><svg viewBox="0 0 24 24"><path d="M12 2a7 7 0 0 0-7 7c0 5 7 13 7 13s7-8 7-13a7 7 0 0 0-7-7z" fill="#e3000f"/><circle cx="12" cy="9" r="2.5" fill="#0f0f0f"/></svg>
      <div><b>Location</b>480 Harbor Park Circle #5 Brookvale, TX 75000</div></div>
    <div class="finfo"><svg viewBox="0 0 24 24"><path d="M6.6 10.8a15 15 0 0 0 6.6 6.6l2.2-2.2a1 1 0 0 1 1-.25 11.4 11.4 0 0 0 3.6.57 1 1 0 0 1 1 1V20a1 1 0 0 1-1 1A17 17 0 0 1 3 4a1 1 0 0 1 1-1h3.5a1 1 0 0 1 1 1c0 1.25.2 2.45.57 3.57a1 1 0 0 1-.25 1z" fill="#e3000f"/></svg>
      <div><b>Phone</b>555.010.9110</div></div>
    <div class="finfo"><svg viewBox="0 0 24 24"><rect x="2" y="5" width="20" height="14" fill="#e3000f"/><path d="M2 5l10 8 10-8" stroke="#0f0f0f" stroke-width="1.6" fill="none"/></svg>
      <div><b>Email</b>hello@haldenauto.example</div></div>
  </div>

  <svg class="abs" style="top:5198px;left:1094px" width="30" height="30" viewBox="0 0 30 30"><circle cx="15" cy="15" r="14" fill="#e3000f"/><path d="M9 18l6-6 6 6" stroke="#fff" stroke-width="2.5" fill="none"/></svg>

  <div class="abs" style="top:5242px;left:0;width:1200px;text-align:center;font-size:12.5px;color:var(--text)">2024 Copyright - Halden Automotive LLC &nbsp;|&nbsp; All Rights Reserved</div>
</div>
</body>
</html>
```